Broschüren-Design für Bettenmanufaktur
Super Design, super schnelle Reaktion, super netter Kontakt!
Zielgruppe
Wir sind eine Bettenmanufaktur die Futonbetten und Himmelbetten aus Metall herstellt, geziert mit Leder- oder Holzelementen an den Bettseiten und Rückenlehnen. Das besondere ist, dass es Systembetten sind. Man kann später aus seinen Futonbett noch ein Himmelbett machen, oder die Leder- und Holzelemente einfach tauschen. Unsere Zielgruppe sind Paare die auf Design und Still stehen, sowie auf Paare die Lust auf Mehr als nur ein Bett haben.
Aufgabenstellung
Bitte an unsere neue Homepage vom Design/Still anpassen: www.trovalin-design.de
Die Broschüre soll als Zulage bei anderen Bestellungen beiliegen und auf Messen verteilt werden.

```html
<!DOCTYPE html>
<html lang="de">
<head>
<meta charset="utf-8">
<title>Trovalin – Metall-Systembett</title>
<link href="https://fonts.googleapis.com/css2?family=Nunito:ital,wght@0,400;0,600;0,800;1,400&family=Roboto+Condensed:wght@700&display=swap" rel="stylesheet">
<style>
  :root{
    --red:#bf3a28;
    --red-soft:#c6412f;
    --dark:#262626;
    --white:#ffffff;
    --black:#111111;
  }
  *{margin:0;padding:0;box-sizing:border-box}
  html,body{width:1200px;height:848px;overflow:hidden;background:var(--red)}
  .brochure{position:relative;width:1200px;height:848px;background:var(--red);font-family:"Nunito",sans-serif;color:var(--white);overflow:hidden}
  .bedroom-photo{position:absolute;left:0;top:0;width:867px;height:763px;
    background:
      radial-gradient(ellipse at 40% 55%, rgba(150,20,20,.55) 0%, rgba(0,0,0,0) 45%),
      radial-gradient(ellipse at 55% 20%, rgba(220,200,190,.35) 0%, rgba(0,0,0,0) 40%),
      linear-gradient(160deg,#9c8f98 0%,#4b3f4a 35%,#231c28 70%,#151218 100%);}
  .partner-name{position:absolute;left:574px;top:44px;font-size:32px;font-weight:600;letter-spacing:.5px;color:var(--white)}
  .brand-box{position:absolute;left:455px;top:191px;width:287px;height:92px;background:var(--white);display:flex;align-items:center;justify-content:center}
  .brand-name{font-family:"Nunito",sans-serif;font-weight:800;font-size:36px;letter-spacing:2px;color:var(--black)}
  .contact{position:absolute;left:400px;width:400px;text-align:center}
  .contact-title{top:364px;font-family:"Roboto Condensed",sans-serif;font-weight:700;font-size:40px;letter-spacing:1px}
  .contact-address{top:431px;font-size:16px;line-height:24.5px;letter-spacing:1px}
  .contact-lines{top:528px;font-size:16px;line-height:24.5px;letter-spacing:1px}
  .feather{position:absolute;background:var(--red-soft);opacity:.6}
  .feather-top{left:868px;top:12px;width:85px;height:122px}
  .feather-bottom{left:1095px;top:630px;width:100px;height:170px}
  .quote-mark{position:absolute;font-family:"Roboto Condensed",sans-serif;font-size:62px;line-height:1;color:var(--white)}
  .quote-top{left:1129px;top:20px}
  .quote-bottom{left:928px;top:628px}
  .tagline{position:absolute;font-style:italic;font-size:29px;letter-spacing:2px;line-height:43px}
  .tagline-top{right:33px;top:65px;text-align:right}
  .tagline-bottom{left:929px;top:672px;line-height:36px;font-size:26px}
  .headline-box{position:absolute;left:800px;top:220px;width:400px;height:392px;background:var(--dark);text-align:center;font-family:"Roboto Condensed",sans-serif;font-weight:700}
  .headline-wishes{margin-top:26px;font-size:52px;line-height:62px;color:var(--red);letter-spacing:1px}
  .headline-product{margin-top:30px;font-size:52px;line-height:61px;color:var(--white);letter-spacing:2px}
  .footer-band{position:absolute;left:0;top:763px;width:1200px;height:85px}
  .footer-line{position:absolute;top:40px;height:1px;background:var(--white)}
  .footer-line.left{left:0;width:243px}
  .footer-line.right{left:575px;width:625px}
  .footer-url{position:absolute;left:243px;width:332px;top:27px;text-align:center;font-size:18px;letter-spacing:2.5px}
</style>
</head>
<body>
<main class="brochure">
  <div class="bedroom-photo" role="img" aria-label="Foto eines schwarzen Metall-Himmelbetts mit weißen Vorhängen, roten Satinkissen und geblümter dunkler Bettwäsche vor gemusterter Tapete"></div>

  <div class="partner-name">lichtfaltwerk</div>

  <div class="brand-box"><span class="brand-name">TROVALIN</span></div>

  <h2 class="contact contact-title">KONTAKT</h2>
  <p class="contact contact-address">Trovalin GmbH<br>Lindenhofweg 12<br>79102 Mühlbach</p>
  <p class="contact contact-lines">Telefon: 0157/30418826 (nur Anrufe)<br>E-Mail: service@trovalin-design.de<br>Website: https://trovalin-design.de</p>

  <div class="feather feather-top" role="img" aria-label="Feder-Strichzeichnung"></div>
  <div class="quote-mark quote-top">&#8220;</div>
  <p class="tagline tagline-top">Futonbett.<br>Himmelbett.<br>Lustbett.</p>

  <section class="headline-box">
    <h1 class="headline-wishes">IHRE WÜNSCHE.<br>IHRE NÄCHTE.<br>IHRE TRÄUME.</h1>
    <p class="headline-product">UNSER METALL-<br>SYSTEMBETT.</p>
  </section>

  <div class="quote-mark quote-bottom">&#8220;</div>
  <p class="tagline tagline-bottom">Sinnlich.<br>Exklusiv.<br>Fesselnd.</p>
  <div class="feather feather-bottom" role="img" aria-label="Feder-Strichzeichnung"></div>

  <footer class="footer-band">
    <span class="footer-line left"></span>
    <span class="footer-url">www.trovalin-design.de</span>
    <span class="footer-line right"></span>
  </footer>
</main>
</body>
</html>
```